A four page single-fold product brochure

The brochure is for a pair of Industrial products. A four page, single fold, post card size brochure preferably with a dark themed, carbon fiber texture background.

I also want to do a spot varnish pattern on the brochure. The varnish effect maybe applied on the image / logo or some accent lines.

I have attached a word documents with pictures and other detailed instructions. Please feel free to contact me if you have any questions. If the images attached won't work for a dark background, please advise.

Thanks, Good Luck!

Industry/Entity Type

Industrial

Requirements
Must have
• Out of the box, modern, special effects

```html
<!DOCTYPE html>
<html lang="en">
<head>
<meta charset="utf-8">
<title>KV-Beacon Brochure Spread</title>
<link href="https://fonts.googleapis.com/css2?family=Carlito:wght@400;700&display=swap" rel="stylesheet">
<style>
  :root {
    --bg-deep: #0b0c0e;
    --bg-mid: #17191c;
    --smoke: rgba(190, 195, 205, 0.16);
    --title-blue: #4fa6e0;
    --sub-blue: #6cb8ec;
    --text: #d9dde2;
    --text-soft: #a9b0b8;
    --rule: rgba(120, 150, 180, 0.35);
    --cell-line: #5d6670;
    --cell-bg: rgba(18, 22, 27, 0.85);
    --head-bg: rgba(30, 35, 42, 0.9);
  }
  * { margin: 0; padding: 0; box-sizing: border-box; }
  html, body { width: 1200px; height: 429px; overflow: hidden; background: var(--bg-deep); }
  body { font-family: "Carlito", "Calibri", sans-serif; color: var(--text); }

  .spread {
    position: relative; width: 1200px; height: 429px; overflow: hidden;
    background: radial-gradient(ellipse at 50% 50%, var(--bg-mid), var(--bg-deep) 75%);
  }
  .smoke { position: absolute; border-radius: 50%; filter: blur(18px); }
  .smoke--a { left: -40px; top: 120px; width: 380px; height: 200px; background: radial-gradient(ellipse, var(--smoke), transparent 70%); }
  .smoke--b { left: 380px; top: -40px; width: 320px; height: 220px; background: radial-gradient(ellipse, var(--smoke), transparent 70%); }
  .smoke--c { left: 740px; top: 60px; width: 420px; height: 300px; background: radial-gradient(ellipse, var(--smoke), transparent 70%); }
  .smoke--d { left: 1010px; top: 250px; width: 240px; height: 200px; background: radial-gradient(ellipse, var(--smoke), transparent 70%); }

  .fold { position: absolute; left: 600px; top: 0; width: 1px; height: 429px; background: rgba(255,255,255,0.06); }
  .frame-line { position: absolute; top: 30px; width: 1px; height: 370px; background: var(--rule); }

  .page { position: absolute; top: 0; height: 429px; }
  .page--left { left: 0; width: 600px; }
  .page--right { left: 600px; width: 600px; }

  .title { position: absolute; font-weight: 400; color: var(--title-blue); white-space: nowrap; }
  .subtitle { position: absolute; color: var(--sub-blue); white-space: nowrap; }

  .product-shot { position: absolute; border-radius: 3px; }
  .product-shot--disposable { left: 106px; top: 97px; width: 80px; height: 86px; background: linear-gradient(135deg, #f4f4f4, #cfd1d4 60%, #8d9096); }
  .product-shot--reusable { left: 421px; top: 97px; width: 91px; height: 86px; background: linear-gradient(135deg, #f2f2f2, #c9cbce 55%, #3a3c40); }

  .features { position: absolute; list-style: none; font-size: 13px; line-height: 17px; color: var(--sub-blue); }
  .features li { position: relative; padding-left: 19px; }
  .features li::before { content: ""; position: absolute; left: 2px; top: 5px; width: 6px; height: 6px; border: 1px solid var(--sub-blue); border-radius: 50%; }

  .spec-table { position: absolute; border-collapse: collapse; table-layout: fixed; font-size: 8.5px; color: var(--text); }
  .spec-table th, .spec-table td { border: 1px solid var(--cell-line); background: var(--cell-bg); text-align: center; vertical-align: middle; line-height: 1.15; padding: 0 3px; }
  .spec-table thead th { background: var(--head-bg); font-weight: 400; }
  .spec-table tbody th { font-weight: 700; }
  .spec-table--right { font-size: 9px; }
  .spec-table--right tbody th { font-size: 10px; }

  .footnotes { position: absolute; font-size: 6.5px; line-height: 8px; color: var(--sub-blue); text-align: center; }
</style>
</head>
<body>
<div class="spread">
  <div class="smoke smoke--a" role="img" aria-label="Soft smoke swirl backdrop"></div>
  <div class="smoke smoke--b" role="img" aria-label="Soft smoke swirl backdrop"></div>
  <div class="smoke smoke--c" role="img" aria-label="Soft smoke swirl backdrop"></div>
  <div class="smoke smoke--d" role="img" aria-label="Soft smoke swirl backdrop"></div>

  <div class="fold"></div>
  <div class="frame-line" style="left:46px"></div>
  <div class="frame-line" style="left:570px; opacity:.5"></div>
  <div class="frame-line" style="left:626px; opacity:.5"></div>
  <div class="frame-line" style="left:1172px"></div>

  <section class="page page--left">
    <h1 class="title" style="left:146px; top:14px; font-size:26px;">KV-Beacon Disposable</h1>
    <p class="subtitle" style="left:180px; top:51px; font-size:14.5px;">World's first Disposable Transmitter</p>

    <div class="product-shot product-shot--disposable" role="img" aria-label="Photo of the disposable transmitter cylinder"></div>

    <ul class="features" style="left:265px; top:113px; width:270px;">
      <li>Highest and Constant signal<br>strength through entire life</li>
      <li>Buy it for the price you rent</li>
      <li>Lower Financial liability</li>
    </ul>

    <table class="spec-table" style="left:171px; top:209px; width:283px;">
      <colgroup><col style="width:95px"><col style="width:62px"><col style="width:62px"><col style="width:64px"></colgroup>
      <thead><tr style="height:17px"><th></th><th>xSD</th><th>SD</th><th>MD</th></tr></thead>
      <tbody>
        <tr style="height:24px"><th>Standard Run-Time¹</th><td>64 hours<br>[2.5 days]</td><td>130 hours<br>[5 days]</td><td>500 hours<br>[21 days]</td></tr>
        <tr style="height:17px"><th>Frequency</th><td colspan="3">ELF ~16Hz to 30 Hz (22Hz default)</td></tr>
        <tr style="height:20px"><th>Pressure</th><td>1800 PSI</td><td>1800 PSI</td><td>1600 PSI</td></tr>
        <tr style="height:20px"><th>Length</th><td>3" [76mm]</td><td>6" [152mm]</td><td>9.5" [241mm]</td></tr>
        <tr style="height:20px"><th>Dia</th><td>1" [25.4mm]</td><td>1.25" [32mm]</td><td>1.875" [48mm]</td></tr>
        <tr style="height:16px"><th>Temperature²</th><td colspan="3">-40°F to 150°F [-40°C to 65°C]</td></tr>
        <tr style="height:15px"><th>Price (USD)</th><td>320</td><td>400</td><td>500</td></tr>
      </tbody>
    </table>

    <p class="footnotes" style="left:165px; top:374px; width:300px;">¹Standard Run-Time is at 25°C. Continuous option available. Longer Run-Times possible with decreased pulse rate.<br>²Run-Times may vary below 32°F [0°C]</p>
  </section>

  <section class="page page--right">
    <h1 class="title" style="left:136px; top:18px; font-size:28px; letter-spacing:.5px;">KV-Beacon Reusable</h1>
    <p class="subtitle" style="left:164px; top:57px; font-size:15px;">Powerful and Economical in one Package</p>

    <div class="product-shot product-shot--reusable" role="img" aria-label="Photo of the reusable transmitter in its open hard case"></div>

    <ul class="features" style="left:94px; top:120px; width:300px;">
      <li>Best signal strength in the industry</li>
      <li>Reliable sealing with spare o-rings</li>
      <li>Includes a Free Ranger style case</li>
    </ul>

    <table class="spec-table spec-table--right" style="left:168px; top:209px; width:289px;">
      <colgroup><col style="width:88px"><col style="width:62px"><col style="width:62px"><col style="width:77px"></colgroup>
      <thead><tr style="height:16px"><th></th><th>xSD</th><th>SD</th><th>MD</th></tr></thead>
      <tbody>
        <tr style="height:24px"><th>Standard Run-Time¹</th><td>64 hours<br>[2.5 days]</td><td>130 hours<br>[5 days]</td><td>500 hours<br>[21 days]</td></tr>
        <tr style="height:13px"><th>Frequency²</th><td colspan="3">ELF ~16Hz to 30 Hz (22Hz default)</td></tr>
        <tr style="height:15px"><th>Pressure</th><td>2000 PSI</td><td>2000 PSI</td><td>2000 PSI</td></tr>
        <tr style="height:23px"><th>Length</th><td>3.4"<br>[86mm]</td><td>6"<br>[152mm]</td><td>9.5" [241mm]</td></tr>
        <tr style="height:23px"><th>Dia</th><td>1"<br>[25.4mm]</td><td>1"<br>[25.4mm]</td><td>1.875" [48mm]</td></tr>
        <tr style="height:14px"><th>Temperature³</th><td colspan="3">-40°F to 150°F [-40°C to 65°C]</td></tr>
        <tr style="height:14px"><th>Price (USD)</th><td>1200</td><td>1400</td><td>1600</td></tr>
      </tbody>
    </table>

    <p class="footnotes" style="left:155px; top:379px; width:315px;">¹ Standard Run-Time is at 25°C. Continuous option available. Longer Run-Times possible with decreased pulse rate.<br>²Higher Pressure rating possible<br>³Run-Times may vary below 32°F [0°C]</p>
  </section>
</div>
</body>
</html>
```